Fontenot Bayou Grillhouse (Owners Card)

Need a classy, but modern business card. I have included a promotional card for the steakhouse. I need one for myself (the owner) that is more professional.

Target Market(s)

General Public

Industry/Entity Type

Food service

Contact Information for Business Card

Name, business address, phone number, email, logo

Font styles to use
Serif
Sans Serif
Decorative
Script

Requirements
Must have
• My name (Darvel Pruitt), business address (327 Oakmere Street), phone number (510) 493-2615, email (Dpruittkr4@mailvane.example. On the back of the card: Psalms 27 1 The LORD is my light and my salvation— whom shall I fear? The LORD is the stronghold of my life— of whom shall I be afraid? 2 When the wicked advance against me to devour me, it is my enemies and my foes who will stumble and fall. 3 Though an army besiege me, my heart will not fear; though war break out against me, even then I will be confident.
Nice to have
• Something that’s bold, but modern and professional.

```html
<!DOCTYPE html>
<html lang="en">
<head>
<meta charset="utf-8">
<title>Fontenot Bayou Grillhouse – Owner Card</title>
<link href="https://fonts.googleapis.com/css2?family=Montserrat:wght@400;500;600;700&display=swap" rel="stylesheet">
<style>
  :root {
    --stage: #8e8e8e;
    --paper: #ffffff;
    --ink: #1a1a1a;
    --leaf: #7fb32a;
    --amber: #f0941e;
    --flame: #e0401f;
    --brand: #c8321c;
    --light: #ffffff;
  }
  * { margin: 0; padding: 0; box-sizing: border-box; }
  html, body { width: 1200px; height: 900px; overflow: hidden; }
  body {
    background: var(--stage);
    font-family: "Montserrat", sans-serif;
    position: relative;
  }
  .card {
    position: absolute;
    width: 560px;
    height: 320px;
    border-radius: 22px;
    overflow: hidden;
    box-shadow: 0 6px 18px rgba(0,0,0,0.25);
  }
  /* Back of card */
  .card-back {
    left: 70px; top: 80px;
    background: linear-gradient(35deg, var(--leaf) 0%, var(--amber) 55%, var(--flame) 100%);
    color: var(--light);
    display: flex; flex-direction: column; align-items: center; justify-content: center;
    padding: 0 40px;
    text-align: center;
  }
  .card-back .brand-name {
    font-weight: 700;
    font-size: 30px;
    letter-spacing: 1px;
    text-transform: uppercase;
    margin-bottom: 26px;
    line-height: 1.1;
  }
  .scripture {
    font-size: 11.5px;
    font-weight: 600;
    line-height: 1.55;
  }
  /* Front of card */
  .card-front {
    left: 570px; top: 500px;
    background: var(--paper);
    color: var(--ink);
  }
  .card-front .brand-name {
    position: absolute;
    left: 34px; top: 70px;
    width: 300px;
    font-weight: 700;
    font-size: 28px;
    line-height: 1.1;
    text-transform: uppercase;
    color: var(--brand);
  }
  .mask-art {
    position: absolute;
    right: 0; top: 0;
    width: 220px; height: 230px;
    border-bottom-left-radius: 120px;
    background: linear-gradient(200deg, var(--flame) 0%, var(--amber) 45%, var(--leaf) 100%);
  }
  .contact {
    position: absolute;
    left: 34px; bottom: 26px;
  }
  .owner-name { font-size: 20px; font-weight: 700; }
  .owner-title { font-size: 12px; margin-bottom: 12px; }
  .address { font-size: 12px; line-height: 1.35; margin-bottom: 10px; }
  .contact-list { list-style: none; font-size: 12px; }
  .contact-list li { display: flex; align-items: center; gap: 8px; line-height: 1.6; }
  .contact-list svg { width: 12px; height: 12px; flex: none; }
</style>
</head>
<body>

<section class="card card-back">
  <h2 class="brand-name">Fontenot Bayou Grillhouse</h2>
  <p class="scripture">
    Psalms 27 1 The LORD is my light and my salvation— whom shall I fear?<br>
    The LORD is the stronghold of my life— of whom shall I be afraid?<br>
    2 When the wicked advance against me to devour me, it is my enemies and<br>
    my foes who will stumble and fall.<br>
    3 Though an army besiege me, my heart will not fear; though war break out<br>
    against me, even then I will be confident.
  </p>
</section>

<section class="card card-front">
  <div class="mask-art" role="img" aria-label="Carnival mask illustration in green-to-orange gradient"></div>
  <h1 class="brand-name">Fontenot Bayou Grillhouse</h1>
  <div class="contact">
    <p class="owner-name">Darvel Pruitt</p>
    <p class="owner-title">Owner</p>
    <p class="address">327 Oakmere Street<br>Marlow Creek, CA 94588</p>
    <ul class="contact-list">
      <li>
        <svg viewBox="0 0 24 24" aria-hidden="true"><path fill="var(--leaf)" d="M6.6 10.8a15.1 15.1 0 0 0 6.6 6.6l2.2-2.2c.3-.3.7-.4 1-.2 1.1.4 2.3.6 3.6.6.6 0 1 .4 1 1V20c0 .6-.4 1-1 1A17 17 0 0 1 3 4c0-.6.4-1 1-1h3.5c.6 0 1 .4 1 1 0 1.3.2 2.5.6 3.6.1.3 0 .7-.2 1z"/></svg>
        (510) 493-2615
      </li>
      <li>
        <svg viewBox="0 0 24 24" aria-hidden="true"><rect x="2" y="5" width="20" height="14" rx="2" fill="var(--amber)"/><path d="M3 6l9 7 9-7" fill="none" stroke="#fff" stroke-width="2"/></svg>
        Dpruittkr4@mailvane.example
      </li>
      <li>
        <svg viewBox="0 0 24 24" aria-hidden="true"><circle cx="12" cy="12" r="10" fill="var(--flame)"/><path d="M2 12h20M12 2c3 3 3 17 0 20M12 2c-3 3-3 17 0 20" fill="none" stroke="#fff" stroke-width="1.5"/></svg>
        www.fontenotbayou.example
      </li>
    </ul>
  </div>
</section>

</body>
</html>
```